Safety Shoes Packaging - Box Design

We need a design for the box of safety shoes.
Our company is active in the industrial and construction sector.
Our brand logo is attached.
Also attached is the hang tag of the working gloves line for some consistency between the brand's product range.
They are intended for use in a wide variety of Industrial environments, like construction, cleaning and maintenance.
The final design should communicate
Safety
heavy duty use & toughness
durability
but also comfort and premium feel.
Packaging should also include a label with the following info - space:
Size:
Model:
Barcode
EN ISO 20345 S3 SRC
CE Symbol
Example of the label is also attached
Target Market(s)
Tradesmen, age 25-50
Industry/Entity Type
Construction, Landscape, Agriculture
Look and feel

```html
<!DOCTYPE html>
<html lang="en">
<head>
<meta charset="utf-8">
<title>Safety Shoe Box – Flat Layout</title>
<link rel="stylesheet" href="https://fonts.googleapis.com/css2?family=Exo+2:wght@400;600;700&display=swap">
<style>
  :root {
    --bg: #e6e4e1;
    --lid-grey: #8e8e8e;
    --lid-grey-light: #a3a3a3;
    --side-dark: #2b2b2b;
    --side-dark-2: #343434;
    --band-black: #141414;
    --orange: #f26a1b;
    --white: #ffffff;
    --tile: #d9d9d9;
    --tile-ink: #333333;
  }
  * { box-sizing: border-box; margin: 0; padding: 0; }
  html, body { width: 1200px; height: 882px; overflow: hidden; }
  body {
    background: var(--bg);
    font-family: "Exo 2", sans-serif;
    position: relative;
  }

  /* Lid top panel */
  .lid-top {
    position: absolute; left: 40px; top: 36px;
    width: 1120px; height: 470px;
    background: var(--lid-grey);
    overflow: hidden;
  }
  .lid-top .boot-art {
    position: absolute; left: 560px; top: 0;
    width: 560px; height: 366px;
    background: linear-gradient(160deg, var(--lid-grey-light), #bdbdbd 60%, #9a9a9a);
  }
  .lid-top .band {
    position: absolute; left: 300px; bottom: 34px;
    width: 820px; height: 70px;
    background: var(--band-black);
    display: flex; align-items: center; justify-content: flex-end;
    padding-right: 60px; gap: 22px;
  }
  .band span, .claim {
    color: var(--orange);
    font-weight: 400;
    font-size: 30px;
    letter-spacing: 1px;
    white-space: nowrap;
  }
  .brand {
    color: var(--orange);
    font-weight: 700;
    letter-spacing: 4px;
    line-height: 1;
    white-space: nowrap;
  }
  .tagline {
    color: var(--white);
    font-weight: 700;
    letter-spacing: 1px;
    white-space: nowrap;
  }
  .lid-top .lockup {
    position: absolute; left: 300px; top: 170px;
  }
  .lid-top .brand { font-size: 96px; }
  .lid-top .tagline { font-size: 30px; margin-top: 6px; }

  /* Box long side */
  .box-side {
    position: absolute; left: 40px; top: 530px;
    width: 860px; height: 316px;
    background: var(--side-dark);
    overflow: hidden;
  }
  .box-side .pattern {
    position: absolute; inset: 0;
    background: linear-gradient(135deg, var(--side-dark-2), var(--side-dark));
  }
  .box-side .lockup {
    position: absolute; left: 50px; top: 116px;
  }
  .box-side .brand { font-size: 70px; letter-spacing: 3px; }
  .box-side .tagline { font-size: 23px; margin-top: 6px; }
  .box-side .claim {
    position: absolute; left: 440px; top: 70px;
    font-size: 21px;
  }
  .features {
    position: absolute; left: 440px; top: 150px;
    display: flex; gap: 10px;
    background: var(--tile); border-radius: 10px;
    padding: 12px 14px;
  }
  .feature { width: 84px; text-align: center; }
  .feature svg { width: 46px; height: 46px; display: block; margin: 0 auto 6px; }
  .feature p { font-size: 12px; color: var(--tile-ink); line-height: 1.15; }

  /* Box end */
  .box-end {
    position: absolute; left: 920px; top: 530px;
    width: 240px; height: 316px;
    background: var(--side-dark);
    padding: 44px 24px;
    overflow: hidden;
  }
  .box-end .brand { font-size: 38px; letter-spacing: 2px; }
  .box-end .tagline { font-size: 14px; margin-top: 6px; }
  .box-end .claim-stack {
    margin-top: 34px;
    color: var(--orange); font-size: 21px; line-height: 1.25;
  }
</style>
</head>
<body>
  <section class="lid-top">
    <div class="boot-art" role="img" aria-label="Line illustration of a laced safety boot on treadplate texture"></div>
    <div class="lockup">
      <div class="brand">TORVAN</div>
      <div class="tagline">BUILT TO PROTECT</div>
    </div>
    <div class="band">
      <span>DURABIL</span><span>COMFORTABLE</span><span>HEAVY DUTY</span>
    </div>
  </section>

  <section class="box-side">
    <div class="pattern" role="img" aria-label="Dark treadplate texture"></div>
    <div class="lockup">
      <div class="brand">TORVAN</div>
      <div class="tagline">BUILT TO PROTECT</div>
    </div>
    <div class="claim">DURABIL&nbsp;&nbsp;COMFORTABLE&nbsp;&nbsp;HEAVY DUTY</div>
    <div class="features">
      <div class="feature">
        <svg viewBox="0 0 46 46"><rect x="2" y="2" width="42" height="42" rx="6" fill="#fff" stroke="#333" stroke-width="2"/><path d="M23 10v20M15 22l8 8 8-8" fill="none" stroke="#333" stroke-width="3"/></svg>
        <p>Impact<br>Protection</p>
      </div>
      <div class="feature">
        <svg viewBox="0 0 46 46"><rect x="2" y="2" width="42" height="42" rx="6" fill="#fff" stroke="#333" stroke-width="2"/><path d="M26 8L14 26h9l-3 12 12-18h-9z" fill="#333"/></svg>
        <p>Antistatic</p>
      </div>
      <div class="feature">
        <svg viewBox="0 0 46 46"><rect x="2" y="2" width="42" height="42" rx="6" fill="#fff" stroke="#333" stroke-width="2"/><path d="M12 12h22L12 20h22L12 28h22L12 36h22" fill="none" stroke="#333" stroke-width="2.5"/></svg>
        <p>Heel Energy<br>Absorption</p>
      </div>
      <div class="feature">
        <svg viewBox="0 0 46 46"><rect x="2" y="2" width="42" height="42" rx="6" fill="#fff" stroke="#333" stroke-width="2"/><path d="M23 9c6 9 10 14 10 19a10 10 0 0 1-20 0c0-5 4-10 10-19z" fill="#333"/></svg>
        <p>Oil<br>Resistant</p>
      </div>
    </div>
  </section>

  <section class="box-end">
    <div class="brand">TORVAN</div>
    <div class="tagline">BUILT TO PROTECT</div>
    <div class="claim-stack">DURABIL<br>COMFORTABLE<br>HEAVY DUTY</div>
  </section>
</body>
</html>
```